Consumer Facing Energy Data Analytics Startup Needs a Postcard to Promote New Product

We need a set of 2 postcards (6 x 4.25 inches as describers in the attached files) to help us promote our product for a new company based in San Francisco called "Lumo Crest".
We develop an alert platform for customers of energy utility companies. Our initial product is "Lumo Notice" - an application that helps people better manage their energy bill by sending an SMS or email alter in advance of a high bill.
We would like to see designs that use the colors blue and orange (same as in the website: www.lumocrest-demo.com). The text of the postcards will be reworked once a layout has been chosen, but we welcome original ways to attract the customers' attention.
Our goal is ultimately to have our targets go the our website and sign up for our service.
The final deliverable should be 8 vector files (preferable .eps, 4 file types, one version in print and one in web format):
- front of card for our small and medium business customers
- front of card for our residential customers
- back of card for our small and medium business customers
- back of card for our residential customers
- DINPro and Avenir

```html
<!DOCTYPE html>
<html lang="en">
<head>
<meta charset="utf-8">
<title>Lumo Crest – Lumo Notice postcards</title>
<link href="https://fonts.googleapis.com/css2?family=Barlow:wght@300;400;600;700&family=Barlow+Condensed:wght@700&display=swap" rel="stylesheet">
<style>
  :root {
    --sky: #3db4d6;
    --blue: #29a3dc;
    --orange: #f9ac3d;
    --ink: #2b2b2b;
    --white: #ffffff;
    --stage: #eeeae5;
    --line: #b9b9b9;
  }
  * { box-sizing: border-box; margin: 0; padding: 0; }
  html, body { width: 902px; height: 1200px; overflow: hidden; }
  body { background: var(--stage); font-family: "Barlow", "Helvetica Neue", Arial, sans-serif; position: relative; }

  .card { position: absolute; width: 652px; overflow: hidden; box-shadow: 0 4px 14px rgba(0,0,0,.18); }
  .card-front { left: 85px; top: 167px; height: 433px; background: var(--sky); }
  .card-back { left: 160px; top: 690px; height: 435px; background: var(--white); }

  /* front */
  .hand-phone { position: absolute; left: 0; top: 80px; width: 240px; height: 309px;
    background: linear-gradient(160deg, #2a2a2a 0 30%, #f7d4bf 30% 100%); opacity: .9; }
  .bubble { position: absolute; left: 22px; top: 14px; width: 114px; height: 80px; background: var(--white);
    border: 3px solid var(--orange); border-radius: 12px; padding: 7px 5px;
    font-size: 10.5px; font-weight: 700; line-height: 1.2; color: var(--ink); text-align: center; }
  .bubble::after { content: ""; position: absolute; left: 64px; bottom: -14px; border: 8px solid transparent;
    border-top: 10px solid var(--orange); }
  .info-panel { position: absolute; left: 278px; top: 0; width: 352px; height: 288px; background: var(--white);
    border-radius: 0 0 10px 10px; }
  .brand { display: flex; align-items: center; gap: 8px; }
  .brand-dot { width: 26px; height: 26px; border-radius: 50%; }
  .brand-name { font-size: 24px; font-weight: 300; letter-spacing: 2px; text-transform: uppercase; }
  .info-panel .brand { position: absolute; left: 95px; top: 28px; }
  .info-panel .brand-dot { background: var(--orange); }
  .info-panel .brand-name { color: var(--blue); }
  .headline { position: absolute; left: 268px; top: 68px; width: 372px; height: 78px; background: var(--orange);
    font-family: "Barlow Condensed", "Arial Narrow", sans-serif; font-weight: 700; color: var(--white);
    font-size: 22px; line-height: 1.05; text-align: center; padding-top: 6px; text-transform: uppercase; letter-spacing: .5px; }
  .section-title { position: absolute; left: 278px; top: 158px; width: 352px; text-align: center;
    font-size: 26px; font-weight: 600; color: var(--blue); }
  .section-title span { color: var(--orange); }
  .about { position: absolute; left: 288px; top: 190px; width: 334px; font-size: 11.2px; line-height: 1.3; color: var(--ink); }
  .about p + p { margin-top: 11px; }
  .appliances { position: absolute; left: 210px; top: 302px; display: flex; gap: 10px; }
  .appliance { width: 75px; height: 75px; }
  .cta-band { position: absolute; left: 0; top: 389px; width: 652px; height: 34px; background: var(--orange);
    color: var(--white); display: flex; align-items: center; gap: 8px; padding-left: 24px; white-space: nowrap; }
  .cta-band .cta { font-size: 16px; font-weight: 600; letter-spacing: .4px; }
  .cta-band .url { font-size: 24px; font-weight: 700; }

  /* back */
  .benefit-panel { position: absolute; left: 0; top: 0; width: 343px; height: 435px; background: var(--blue); }
  .benefit-panel .brand { position: absolute; left: 16px; top: 22px; }
  .benefit-panel .brand-dot { background: var(--white); }
  .benefit-panel .brand-name { color: var(--white); }
  .benefit-title { position: absolute; left: 15px; top: 96px; font-size: 28px; font-weight: 700; color: var(--orange); }
  .benefits { position: absolute; left: 22px; top: 136px; list-style: none; }
  .benefit { display: flex; align-items: center; height: 58px; }
  .benefit svg { width: 48px; height: 48px; flex: none; }
  .benefit span { margin-left: 20px; width: 245px; color: var(--white); font-size: 12px; font-weight: 700; line-height: 1.15; }
  .url-ribbon { position: absolute; left: 0; top: 375px; width: 366px; height: 46px; background: var(--orange);
    clip-path: polygon(0 0, 100% 0, 94% 50%, 100% 100%, 0 100%); color: var(--white);
    font-size: 25px; font-weight: 700; line-height: 46px; padding-left: 12px; white-space: nowrap; }
  .stamp-box { position: absolute; left: 540px; top: 27px; width: 83px; height: 83px; border: 1.5px solid var(--line); }
</style>
</head>
<body>

<section class="card card-front">
  <div class="hand-phone" role="img" aria-label="Illustration of a hand holding a smartphone showing the app"></div>
  <div class="bubble">Get your alerts on the go by email or SMS so you're always in control</div>

  <div class="info-panel">
    <div class="brand"><span class="brand-dot"></span><span class="brand-name">Lumo Crest</span></div>
  </div>
  <h1 class="headline">Never get the bad surprise<br>of high energy bill again<br>with Lumo Notice</h1>
  <h2 class="section-title">WHAT <span>WE DO</span></h2>
  <div class="about">
    <p>Lumo Crest helps you predict and avoid your high energy bills.</p>
    <p>Lumo Crest employs advanced analytics software to assess customer energy use on a daily basis. We predict monthly energy bills based on current usage, and provide customer alerts and tips when use is above normal.</p>
  </div>

  <div class="appliances">
    <svg class="appliance" viewBox="0 0 75 75" aria-label="Washing machine"><circle cx="37.5" cy="37.5" r="35" fill="none" stroke="#fff" stroke-width="3"/><rect x="24" y="18" width="27" height="38" rx="2" fill="#fff"/><circle cx="37.5" cy="41" r="8" fill="none" stroke="#3db4d6" stroke-width="2"/><line x1="24" y1="26" x2="51" y2="26" stroke="#3db4d6" stroke-width="1.5"/></svg>
    <svg class="appliance" viewBox="0 0 75 75" aria-label="Vacuum cleaner"><circle cx="37.5" cy="37.5" r="35" fill="none" stroke="#fff" stroke-width="3"/><circle cx="30" cy="44" r="10" fill="#fff"/><path d="M38 40 C46 30 48 22 52 18 M50 55 L58 55" stroke="#fff" stroke-width="3" fill="none" stroke-linecap="round"/><path d="M38 40 Q48 52 54 55" stroke="#fff" stroke-width="2" fill="none"/></svg>
    <svg class="appliance" viewBox="0 0 75 75" aria-label="Television"><circle cx="37.5" cy="37.5" r="35" fill="none" stroke="#fff" stroke-width="3"/><rect x="17" y="22" width="41" height="26" rx="2" fill="none" stroke="#fff" stroke-width="3.5"/><rect x="33" y="49" width="9" height="5" fill="#fff"/><rect x="27" y="54" width="21" height="3" fill="#fff"/></svg>
    <svg class="appliance" viewBox="0 0 75 75" aria-label="Oven"><circle cx="37.5" cy="37.5" r="35" fill="none" stroke="#fff" stroke-width="3"/><rect x="23" y="18" width="29" height="39" fill="#fff"/><rect x="27" y="31" width="21" height="20" fill="none" stroke="#3db4d6" stroke-width="2"/><circle cx="29" cy="24" r="2" fill="#3db4d6"/><circle cx="37.5" cy="24" r="2" fill="#3db4d6"/><circle cx="46" cy="24" r="2" fill="#3db4d6"/></svg>
    <svg class="appliance" viewBox="0 0 75 75" aria-label="Refrigerator"><circle cx="37.5" cy="37.5" r="35" fill="none" stroke="#fff" stroke-width="3"/><rect x="27" y="15" width="21" height="44" rx="2" fill="#fff"/><line x1="27" y1="30" x2="48" y2="30" stroke="#3db4d6" stroke-width="2"/><line x1="31" y1="20" x2="31" y2="26" stroke="#3db4d6" stroke-width="2"/><line x1="31" y1="35" x2="31" y2="43" stroke="#3db4d6" stroke-width="2"/></svg>
  </div>

  <div class="cta-band"><span class="cta">SIGN UP FOR LUMO NOTICE NOW!</span><span class="url">www.lumocrest-demo.com</span></div>
</section>

<section class="card card-back">
  <div class="benefit-panel">
    <div class="brand"><span class="brand-dot"></span><span class="brand-name">Lumo Crest</span></div>
    <h2 class="benefit-title">BENEFIT FOR YOU</h2>
    <ul class="benefits">
      <li class="benefit">
        <svg viewBox="0 0 48 48" aria-hidden="true"><circle cx="24" cy="24" r="22" fill="#fff"/><g stroke="#29a3dc" stroke-width="2"><line x1="13" y1="17" x2="35" y2="17"/><line x1="13" y1="24" x2="35" y2="24"/><line x1="13" y1="31" x2="35" y2="31"/></g><g fill="#29a3dc"><rect x="17" y="14" width="4" height="6"/><rect x="27" y="21" width="4" height="6"/><rect x="21" y="28" width="4" height="6"/></g></svg>
        <span>More control over your energy bill</span>
      </li>
      <li class="benefit">
        <svg viewBox="0 0 48 48" aria-hidden="true"><circle cx="24" cy="24" r="22" fill="#fff"/><rect x="12" y="18" width="24" height="16" fill="none" stroke="#29a3dc" stroke-width="2"/><path d="M12 18 L24 28 L36 18" fill="none" stroke="#29a3dc" stroke-width="2"/><text x="24" y="16" font-size="10" font-weight="700" fill="#29a3dc" text-anchor="middle" font-family="Barlow, sans-serif">$</text></svg>
        <span>You will not get an unpleasant surprise on their next bill</span>
      </li>
      <li class="benefit">
        <svg viewBox="0 0 48 48" aria-hidden="true"><circle cx="24" cy="24" r="22" fill="#fff"/><path d="M15 22 A10 10 0 1 0 22 14" fill="none" stroke="#29a3dc" stroke-width="3"/><path d="M18 10 L24 14 L19 19" fill="none" stroke="#29a3dc" stroke-width="2.5"/><text x="25" y="30" font-size="13" font-weight="700" fill="#29a3dc" text-anchor="middle" font-family="Barlow, sans-serif">$</text></svg>
        <span>Learn about your energy usage and cost</span>
      </li>
      <li class="benefit">
        <svg viewBox="0 0 48 48" aria-hidden="true"><circle cx="24" cy="24" r="22" fill="#fff"/><circle cx="24" cy="22" r="7" fill="none" stroke="#29a3dc" stroke-width="2"/><rect x="21" y="30" width="6" height="5" fill="#29a3dc"/><g stroke="#29a3dc" stroke-width="1.5"><line x1="24" y1="9" x2="24" y2="12"/><line x1="13" y1="22" x2="10" y2="22"/><line x1="35" y1="22" x2="38" y2="22"/><line x1="16" y1="14" x2="14" y2="12"/><line x1="32" y1="14" x2="34" y2="12"/></g></svg>
        <span>Learn about new ways to save, specific to your habits</span>
      </li>
    </ul>
  </div>
  <div class="url-ribbon">www.lumocrest-demo.com</div>
  <div class="stamp-box"></div>
</section>

</body>
</html>
```